Trevolina corporate powerpoint

Hi,
I am creating my own web3 and blockchain academy.

I would like to obtain pricing for a complete corporate powerpoint template for my training sessions in companies and bussiness schools

. I am sharing with you my logo in order to show you my colours.
If you can improve my logo, it will be perfect too. (full pack to launch it)

Thanks
Updates

designers are asiking for an extension

Target Market(s)

Companies and Business Schools

Industry/Entity Type

academy

Font styles to use
Sans Serif
Other font styles liked:
• Arial, Calibri

Colors
0054AA
0677BA
7BADD7
CADEEF
E8F1F8
0094D4
00A9DD
6FCCEA
C7EBF8
E9F6FB
00AB8E
00BBA5
67D7C9
C6EFE9
E9F9F6
F0912C
F2A743
F7CA91
FBE8D2
FDF5EE
EE7325
F08F49
F5BC92
FAE3D3
FDF4ED
6B429C
8869AF
B7A5CE
E3DAEB
F3F0F8

Requirements
Must have
• Blockchain thematic, withe and dark (not black) slides

```html
<!DOCTYPE html>
<html lang="en">
<head>
<meta charset="utf-8">
<title>Trevolina – Corporate Presentation Template</title>
<link rel="stylesheet" href="https://fonts.googleapis.com/css2?family=Poppins:ital,wght@0,300;0,400;0,500;0,600;0,700;0,800;1,500&display=swap">
<style>
  :root{
    --navy:#0a1c4a;
    --navy-deep:#06112e;
    --blue:#0054aa;
    --blue-mid:#0677ba;
    --blue-royal:#0d3a9a;
    --sky:#7badd7;
    --ice:#cadeef;
    --mist:#e8f1f8;
    --teal:#00ab8e;
    --cyan:#00a9dd;
    --mint-soft:#e9f9f6;
    --orange:#ee7325;
    --orange-warm:#f0912c;
    --white:#ffffff;
    --ink:#1c2b4a;
    --grey:#5a6478;
    --page:#f2f3f5;
  }
  *{box-sizing:border-box;margin:0;padding:0}
  html,body{width:1200px;height:3648px;overflow:hidden;background:var(--page);font-family:"Poppins",Arial,sans-serif;color:var(--ink)}
  .deck{position:relative;width:1200px;height:3648px}
  .slide{position:absolute;left:100px;width:1000px;height:563px;overflow:hidden}
  .abs{position:absolute}
  .photo{position:absolute}

  /* Slide 1 — Title */
  .s-title{top:48px;background:var(--navy-deep)}
  .s-title .photo{left:420px;top:0;width:580px;height:563px;background:radial-gradient(circle at 50% 40%,#5d6b86 0%,#27324d 30%,#0d1630 65%,#070d20 100%)}
  .s-title .accent{left:0;top:0;width:440px;height:400px;background:linear-gradient(180deg,var(--orange) 0%,#b5582a 45%,#1c2450 100%)}
  .s-title .shade{left:0;top:0;width:560px;height:563px;background:linear-gradient(90deg,rgba(6,17,46,.25) 0%,rgba(6,17,46,0) 100%)}
  .s-title h1{left:30px;top:210px;color:var(--white);font-weight:800;font-size:54px;line-height:1;letter-spacing:.5px}
  .s-title .sub{left:30px;top:330px;width:400px;color:var(--white);font-weight:600;font-size:17px;line-height:1.35}
  .brand{left:470px;top:248px;display:flex;align-items:center;gap:8px;color:var(--white);font-weight:700;font-size:16px}
  .brand .mark{width:14px;height:14px;background:var(--orange)}

  /* Slide 2 — About */
  .s-about{top:647px;background:var(--mist)}
  .s-about h2{left:24px;top:28px;color:var(--blue);font-weight:800;font-size:28px;line-height:1.08}
  .s-about .body{left:24px;top:104px;width:440px;font-size:12px;line-height:1.6;color:var(--grey)}
  .s-about h3{left:24px;top:228px;color:var(--blue);font-weight:700;font-size:16px}
  .bullets{left:24px;top:262px;list-style:none;font-size:12px;color:var(--grey)}
  .bullets li{display:flex;align-items:center;gap:10px;height:28px}
  .bullets svg{flex:none}
  .s-about .photo{left:500px;top:0;width:500px;height:460px;background:radial-gradient(circle at 55% 45%,#8fb3e0 0%,#2e5aa8 35%,#0b1f56 75%)}
  .quote{padding:26px 34px;background:var(--orange);color:var(--white);font-style:italic;font-weight:500;font-size:16px;line-height:1.45}
  .s-about .quote{left:510px;top:424px;width:490px;height:139px}

  /* Slide 3 — Features */
  .s-feat{top:1246px;background:linear-gradient(135deg,#0d4fa0 0%,#0677ba 45%,#0a9e9e 100%)}
  .s-feat h2{left:0;top:52px;width:1000px;text-align:center;color:var(--white);font-weight:800;font-size:32px;line-height:1.2}
  .panel{left:0;top:180px;width:948px;height:228px;background:var(--mint-soft);border-radius:0 114px 114px 0}
  .cards{left:40px;top:206px;display:flex;gap:14px}
  .card{width:206px;height:176px;background:var(--white);border-radius:6px;box-shadow:0 2px 8px rgba(0,40,90,.12);text-align:center;padding:20px 12px 0}
  .card svg{display:block;margin:0 auto 12px}
  .card h4{font-weight:700;font-size:13px;color:var(--ink);margin-bottom:6px}
  .card p{font-size:10.5px;line-height:1.45;color:var(--grey)}
  .card + .card{border-left:1px solid #e3e8ee}
  .s-feat .note{left:150px;top:456px;width:700px;text-align:center;color:var(--white);font-size:12px;line-height:1.6}

  /* Slide 4 — Split */
  .s-split{top:1845px;background:var(--mist)}
  .s-split .photo-left{left:0;top:0;width:312px;height:460px;background:linear-gradient(160deg,#d9dde6 0%,#7d8aa3 40%,#2a3a5e 100%)}
  .s-split .photo-right{left:690px;top:100px;width:310px;height:420px;background:linear-gradient(150deg,#c9a577 0%,#e7d9c2 45%,#9a8a78 100%)}
  .s-split h2{left:340px;top:100px;width:330px;text-align:center;color:var(--blue);font-weight:800;font-size:26px;line-height:1.2}
  .s-split .body{left:345px;top:236px;width:320px;text-align:center;font-size:12px;line-height:1.65;color:var(--grey)}

  /* Slide 5 — Icons & text */
  .s-net{top:2444px;background:var(--blue-royal)}
  .s-net .photo{left:0;top:0;width:500px;height:420px;background:radial-gradient(circle at 45% 50%,#e8eef7 0%,#9fb3d4 35%,#2c4a86 80%)}
  .s-net .quote{left:0;top:420px;width:500px;height:143px}
  .s-net h2{left:540px;top:112px;width:430px;text-align:center;color:var(--white);font-weight:800;font-size:26px;line-height:1.2}
  .s-net .body{left:560px;top:236px;width:390px;text-align:center;font-size:12px;line-height:1.65;color:#dfe8f7}

  /* Slide 6 — Thank you */
  .s-thanks{top:3043px;background:var(--navy-deep)}
  .s-thanks .photo{left:0;top:0;width:1000px;height:563px;background:radial-gradient(ellipse at 50% 55%,#123a8a 0%,#0a1d52 45%,#050c24 100%)}
  .s-thanks h2{left:0;top:124px;width:1000px;text-align:center;color:var(--white);font-weight:800;font-size:48px;letter-spacing:1px}
  .s-thanks .lead{left:150px;top:198px;width:700px;text-align:center;color:var(--white);font-weight:400;font-size:34px;line-height:1.25}
  .contact{left:0;width:1000px;display:flex;justify-content:center;align-items:center;gap:14px;color:var(--white);font-size:17px}
  .contact strong{font-weight:700}
  .contact .ico{width:36px;height:36px;border-radius:50%;background:var(--white);display:flex;align-items:center;justify-content:center}
  .c-phone{top:326px}
  .c-mail{top:386px}
</style>
</head>
<body>
<main class="deck">

  <section class="slide s-title">
    <div class="photo" role="img" aria-label="Glowing wireframe cube on a dark technology background"></div>
    <div class="abs accent"></div>
    <div class="abs shade"></div>
    <h1 class="abs">TREVOLINA<br>ACADEMY</h1>
    <p class="abs sub">Neque porro quisquam est qui dolorem ipsum quia dolor sit.</p>
    <div class="abs brand"><span class="mark"></span>Trevolina</div>
  </section>

  <section class="slide s-about">
    <h2 class="abs">ABOUT<br>TREVOLINA</h2>
    <p class="abs body">Sed ut perspiciatis unde omnis iste natus error sit voluptatem accusantium doloremque laudantium, totam rem aperiam, eaque ipsa quae ab illo inventore veritatis et quasi architecto beatae vitae dicta sunt explicabo. Nemo enim ipsam voluptatem quia voluptas sit aspernatur aut odit aut fugit, sed quia consequuntur magni dolores eos.</p>
    <h3 class="abs">Sed ut perspiciatis unde omnis iste</h3>
    <ul class="abs bullets">
      <li><svg width="8" height="10" viewBox="0 0 8 10"><path d="M0 0L8 5L0 10Z" fill="#ee7325"/></svg>Natus error sit voluptatem</li>
      <li><svg width="8" height="10" viewBox="0 0 8 10"><path d="M0 0L8 5L0 10Z" fill="#ee7325"/></svg>Accusantium doloremque laudantium</li>
      <li><svg width="8" height="10" viewBox="0 0 8 10"><path d="M0 0L8 5L0 10Z" fill="#ee7325"/></svg>Totam rem aperiam, eaque ipsa quae ab illo</li>
      <li><svg width="8" height="10" viewBox="0 0 8 10"><path d="M0 0L8 5L0 10Z" fill="#ee7325"/></svg>Inventore veritatis et quasi architecto</li>
      <li><svg width="8" height="10" viewBox="0 0 8 10"><path d="M0 0L8 5L0 10Z" fill="#ee7325"/></svg>Beatae vitae dicta sunt explicabo nemo ipsam</li>
      <li><svg width="8" height="10" viewBox="0 0 8 10"><path d="M0 0L8 5L0 10Z" fill="#ee7325"/></svg>Voluptatem quia voluptas sit aspernat</li>
    </ul>
    <div class="photo" role="img" aria-label="Cluster of glowing blue data cubes"></div>
    <blockquote class="abs quote">“ Sed ut perspiciatis unde omnis iste natus error sit voluptatem accusantium doloremque laudantium, totam rem aperiam, eaque ipsa quae ab illo.”</blockquote>
  </section>

  <section class="slide s-feat">
    <h2 class="abs">NEMO ENIM IPSAM<br>VOLUPTATEM</h2>
    <div class="abs panel"></div>
    <div class="abs cards">
      <article class="card">
        <svg width="40" height="40" viewBox="0 0 40 40" fill="none" stroke="#ee7325" stroke-width="2"><rect x="14" y="4" width="12" height="10"/><rect x="3" y="26" width="12" height="10"/><rect x="25" y="26" width="12" height="10"/><path d="M20 14V20M9 26V20H31V26"/></svg>
        <h4>Nemo Enim Psam</h4>
        <p>Neque porro quisquam est qui dolorem ipsum quia dolor sit amet.</p>
      </article>
      <article class="card">
        <svg width="40" height="40" viewBox="0 0 40 40" fill="none" stroke="#ee7325" stroke-width="2"><rect x="4" y="8" width="32" height="22" rx="2"/><path d="M14 36H26M20 30V36M10 22L16 16L22 20L30 13"/></svg>
        <h4>Nemo Enim Psam</h4>
        <p>Neque porro quisquam est qui dolorem ipsum quia dolor sit amet.</p>
      </article>
      <article class="card">
        <svg width="40" height="40" viewBox="0 0 40 40" fill="none" stroke="#ee7325" stroke-width="2"><rect x="8" y="4" width="24" height="32" rx="2"/><path d="M13 12H27M13 18H27M13 24H22"/><path d="M24 28L27 31L33 24"/></svg>
        <h4>Nemo Enim Psam</h4>
        <p>Neque porro quisquam est qui dolorem ipsum quia dolor sit amet.</p>
      </article>
      <article class="card">
        <svg width="40" height="40" viewBox="0 0 40 40" fill="none" stroke="#ee7325" stroke-width="2"><circle cx="20" cy="16" r="10"/><path d="M15 28H25M16 33H24M17 16L20 19L24 13"/></svg>
        <h4>Nemo Enim Psam</h4>
        <p>Neque porro quisquam est qui dolorem ipsum quia dolor sit amet.</p>
      </article>
    </div>
    <p class="abs note">Sed ut perspiciatis unde omnis iste natus error sit voluptatem accusantium doloremque laudantium, totam rem aperiam, eaque ipsa quae ab illo inventore veritatis et quasi architecto beatae vitae dicta sunt explicabo.</p>
  </section>

  <section class="slide s-split">
    <div class="photo photo-left" role="img" aria-label="Professional working with a laptop in front of a blockchain graphic"></div>
    <h2 class="abs">NEMO ENIM IPS<br>VOLUPTATEM QUIA<br>VOLUPTAS</h2>
    <p class="abs body">Sed ut perspiciatis unde omnis iste natus error sit voluptatem accusantium doloremque laudantium, totam rem aperiam, eaque ipsa quae ab illo inventore veritatis et quasi architecto beatae vitae dicta sunt explicabo. Nemo enim ipsam voluptatem quia voluptas sit aspernatur aut odit aut fugit, sed quia consequuntur magni.</p>
    <div class="photo photo-right" role="img" aria-label="Handwritten note about blockchain basics on a desk with a pen"></div>
  </section>

  <section class="slide s-net">
    <div class="photo" role="img" aria-label="Blockchain network diagram with connected technology icons"></div>
    <blockquote class="abs quote">“ Sed ut perspiciatis unde omnis iste natus error sit voluptatem accusantium doloremque laudantium, totam rem aperiam, eaque ipsa quae ab illo.”</blockquote>
    <h2 class="abs">NEMO ENIM IPS<br>VOLUPTATEM QUIA<br>VOLUPTAS</h2>
    <p class="abs body">Sed ut perspiciatis unde omnis iste natus error sit voluptatem accusantium doloremque laudantium, totam rem aperiam, eaque ipsa quae ab illo inventore veritatis et quasi architecto beatae vitae dicta sunt explicabo. Nemo enim ipsam voluptatem quia voluptas sit aspernatur aut odit aut fugit, sed quia consequuntur magni.</p>
  </section>

  <section class="slide s-thanks">
    <div class="photo" role="img" aria-label="Glowing blue chain links on a dark background"></div>
    <h2 class="abs">THANK YOU</h2>
    <p class="abs lead">Quis autem vel eum iure reprehenderit qui in ea voluptate.</p>
    <div class="abs contact c-phone">
      <span class="ico"><svg width="18" height="18" viewBox="0 0 24 24"><path d="M6.6 10.8a15.1 15.1 0 006.6 6.6l2.2-2.2a1 1 0 011-.25 11.4 11.4 0 003.6.57 1 1 0 011 1V20a1 1 0 01-1 1A17 17 0 013 4a1 1 0 011-1h3.5a1 1 0 011 1c0 1.25.2 2.45.57 3.57a1 1 0 01-.25 1z" fill="#06112e"/></svg></span>
      <span><strong>Phone:</strong> 1-800-555-0142</span>
    </div>
    <div class="abs contact c-mail">
      <span class="ico"><svg width="18" height="18" viewBox="0 0 24 24"><rect x="3" y="5" width="18" height="14" rx="2" fill="#06112e"/><path d="M4 7l8 6 8-6" fill="none" stroke="#fff" stroke-width="1.6"/></svg></span>
      <span><strong>Email:</strong> hello@trevolina.com</span>
    </div>
  </section>

</main>
</body>
</html>
```